Dental Patient Education Single page-Multiple pages needed.

I am creating a unique dental patient education materials for resale. I work in the dental industry, training dentists and thier teams how to improve patient acceptance rates for treatment. I see a need that all patient education material is designed incorrectly. I want to fix this by creating patient education material that educated patients based on all of the treatment options for a diagnosed condition. Tradidional patient education material reads like a catalog of procedures. This format is not effective for helping the patient quickly understand the consequences of non treatment and the benefits and disadvantages of their treatment options. Specifics of the Job:The design images must be royalty free.I will provide the text.Initially there are for major diagnosed conditions: Infected Tooth Treatment Options, Single to Multiple Missing tooth Treatment Options, Full Arch of Missing Teeth Treatment Options, and Full Arch Fixed Dental Implant Treatment OptionsThe layout should mirror the attached sample of Single Missing Tooth Treatment Options.This is a project that will require edits and redesigned based on testing.I also need this in Adobe, so it can be customized/branded for a dental office.

Target Market(s)

Dental office professionals to educate patients.

Font styles to use
Sans Serif

Colors
3277b5

Requirements
Must have
• Professional look and feel
• Royalty free images
• Easy to read

```html
<!DOCTYPE html>
<html lang="en">
<head>
<meta charset="utf-8">
<title>Single Missing Tooth – Treatment Options</title>
<link href="https://fonts.googleapis.com/css2?family=Source+Sans+3:wght@400;600;700&display=swap" rel="stylesheet">
<style>
  :root {
    --navy: #2b3491;
    --navy-dark: #232b7c;
    --text: #3a3a3a;
    --sky-1: #ffffff;
    --sky-2: #e4eef7;
    --sky-3: #c9dcec;
    --rule-grey: #b9bcc4;
    --paper: #ffffff;
    --gum: #e9a3a6;
    --enamel: #f5f3ef;
  }
  * { box-sizing: border-box; margin: 0; padding: 0; }
  html, body { width: 1060px; height: 1200px; overflow: hidden; background: var(--paper); }
  body { font-family: "Source Sans 3", sans-serif; color: var(--text); position: relative; }

  .header {
    position: absolute; inset: 0 0 auto 0; height: 440px;
    background: linear-gradient(180deg, var(--sky-1) 0%, var(--sky-2) 60%, var(--sky-3) 100%);
  }
  .hero-photo {
    position: absolute; top: 0; right: 0; width: 560px; height: 420px;
    background: radial-gradient(ellipse at 55% 35%, #f7f3f1 0%, #eed6cf 30%, #d9b6ad 45%, #dbe8f3 75%, #d2e2f0 100%);
  }
  .wave { position: absolute; left: 0; top: 300px; width: 1060px; height: 150px; }

  .intro { position: absolute; left: 40px; top: 64px; width: 450px; }
  .intro-title { color: var(--navy); font-weight: 700; font-size: 46px; line-height: 1.05; }
  .intro-subtitle { color: var(--navy); font-weight: 700; font-size: 26px; margin-top: 8px; letter-spacing: .2px; }
  .intro-text { color: var(--navy); font-weight: 600; font-size: 15.5px; line-height: 1.4; margin-top: 26px; }
  .intro-text + .intro-text { margin-top: 18px; }

  .option { position: absolute; width: 470px; }
  .option-1 { left: 40px; top: 452px; }
  .option-2 { left: 550px; top: 452px; }
  .option-3 { left: 40px; top: 826px; }
  .option-4 { left: 550px; top: 826px; }

  .option-head { position: relative; height: 130px; }
  .option-label {
    position: absolute; left: 0; top: 52px; height: 32px; width: 260px;
    background: var(--navy); color: #fff; border-radius: 16px 0 0 16px;
    padding-left: 14px; display: flex; align-items: center; font-size: 17px; white-space: nowrap;
  }
  .option-label strong { font-weight: 700; margin-right: 5px; }
  .option-label .small { font-size: 12px; line-height: 1; font-weight: 600; }
  .option-figure {
    position: absolute; left: 236px; top: 0; width: 132px; height: 132px; border-radius: 50%;
    border: 4px solid var(--navy); background: var(--paper); overflow: hidden;
  }
  .option-figure .art {
    position: absolute; inset: 14px; border-radius: 50%;
    background: radial-gradient(ellipse at 50% 40%, var(--enamel) 0%, var(--enamel) 35%, var(--gum) 65%, #fff 100%);
  }
  .option-body { margin-top: 14px; font-size: 16.5px; line-height: 1.42; text-align: justify; }
  .option-body p + p { margin-top: 20px; }
  .option-body b { font-weight: 700; }

  .footer-band { position: absolute; left: 0; right: 0; bottom: 0; height: 30px; background: var(--navy-dark); }
</style>
</head>
<body>
  <header class="header">
    <div class="hero-photo" role="img" aria-label="Photo of a smiling patient's mouth with a dental mirror"></div>
    <svg class="wave" viewBox="0 0 1060 150" aria-hidden="true">
      <path d="M0 70 C 260 140, 520 130, 720 70 S 960 -5 1060 10 L1060 150 L0 150 Z" fill="#ffffff"/>
      <path d="M0 62 C 260 132, 520 122, 720 62 S 960 -13 1060 2" fill="none" stroke="var(--rule-grey)" stroke-width="4"/>
      <path d="M250 112 C 420 128, 570 112, 720 70 S 960 -5 1060 10" fill="none" stroke="var(--navy)" stroke-width="8"/>
    </svg>
    <div class="intro">
      <h1 class="intro-title">Single Missing Tooth</h1>
      <h2 class="intro-subtitle">YOUR OTION FOR TREATMENT</h2>
      <p class="intro-text">A missing tooth is a serious issue. It can cause long-term damage to facial structure, bone density and your ability to feel confident in your smile.</p>
      <p class="intro-text"><strong>Maple Grove Dental</strong> has several options available to fix your missing tooth.</p>
    </div>
  </header>

  <section class="option option-1">
    <div class="option-head">
      <div class="option-label"><strong>OPTION 1</strong> - Do Nothing</div>
      <div class="option-figure"><div class="art" role="img" aria-label="Illustration of a dental arch with one tooth missing"></div></div>
    </div>
    <div class="option-body">
      <p>If you choose to do nothing at this time, the cost down the road can be substantial.</p>
      <p><b>$10,000+</b> for orthodontics to straighten out the teeth, implant, abutment and crown, bone grafting and possible sinus lift to replace lost bone.</p>
    </div>
  </section>

  <section class="option option-2">
    <div class="option-head">
      <div class="option-label"><strong>OPTION 2</strong> - Dental Implant</div>
      <div class="option-figure"><div class="art" role="img" aria-label="Illustration of a dental implant placed in the jaw"></div></div>
    </div>
    <div class="option-body">
      <p>The bad news is that a dental implant is the most expensive option, <b>BUT</b> the good news is it is the most effective, functional and aesthetically pleasing. A dental implant will keep the bone in that area of the jaw from atrophy. It helps maintain face shape and prevents 'sunken face'. The implant will prevent surrounding teeth from shifting and chances of losing the tooth decline. It will keep the teeth from shifting, and will prevent any future need to cut down the adjacent teeth. A dental implant is the nearest thing to a natural tooth available today.</p>
    </div>
  </section>

  <section class="option option-3">
    <div class="option-head">
      <div class="option-label"><strong>OPTION 3</strong> - Dental Bridge</div>
      <div class="option-figure"><div class="art" role="img" aria-label="Illustration of a three-unit dental bridge"></div></div>
    </div>
    <div class="option-body">
      <p>The good news here is that a bridge is less expensive than the implant option <b>BUT</b> you will continue to lose bone in that area over time. Food will get caught in the hard to reach areas and if not cleaned properly could mean you have to replace the bridge every 7 years. In addition, to secure the bridge, the adjacent teeth must be cut down in order to be used as anchors for the appliance. Why cut down two good teeth if we don't have to?</p>
    </div>
  </section>

  <section class="option option-4">
    <div class="option-head">
      <div class="option-label"><strong>OPTION 4</strong> - <span class="small">The Removable Partial<br>Denture (RPO)</span></div>
      <div class="option-figure"><div class="art" role="img" aria-label="Illustration of a removable partial denture"></div></div>
    </div>
    <div class="option-body">
      <p>The good news here is that it's the least expensive option of the 3, but the <b>BAD</b> news is that your teeth have to come out every night. You won't be able to chew your food as well and your tongue will be uncomfortable with the big, bulky plastic sitting in your mouth all day.</p>
    </div>
  </section>

  <div class="footer-band"></div>
</body>
</html>
```